Daniel Fordyce Psychotherapy Business Card Design Project

I need a welcoming business card for a Somatic Psychotherapy private practice based in Melbourne, Australia. I help individual clients to work through issues in their life that are inhibiting achieving their full potential. I would like a san serif font and the oculars are:
blue: R:37 G:61 B:95 C:93 M:77 Y:38 K:28
orange: R:241 G:103 B:43 C:0 M:74 Y:93 K:0
The final design should communicate warm, welcoming and safe environment in which clients are supported to grow. It should also convey a collaborative approach to achieve success between me (the therapist) and the client. The uploaded file is my new logo. Also an organic look and feel while maintaining professionalism and a clean, simple look is sought after.
In addition to the logo my details are:
Daniel Fordyce
Psychotherapist
B.Arts., Grad Dip. T&D., Dip.Som.Psych, MRTOB, MFLENG
0417 552 908
dfordyce@danielfordyce.com.au
www.danielfordyce.com.au
Psychotherapy Clients
Environment

```html
<!DOCTYPE html>
<html lang="en">
<head>
<meta charset="utf-8">
<title>Daniel Fordyce Psychotherapy – Business Card</title>
<link href="https://fonts.googleapis.com/css2?family=Arimo:wght@400;700&display=swap" rel="stylesheet">
<style>
  :root {
    --navy: #253d5f;
    --orange: #f1672b;
    --white: #ffffff;
    --black: #111111;
    --grey: #8a8d91;
    --backdrop: #e9eaec;
  }
  * { box-sizing: border-box; margin: 0; padding: 0; }
  html, body { width: 1200px; height: 900px; overflow: hidden; }
  body {
    background: var(--backdrop);
    font-family: "Arimo", Arial, sans-serif;
    position: relative;
  }
  .card {
    position: absolute;
    left: 250px;
    width: 700px;
    height: 400px;
    border-radius: 24px;
    overflow: hidden;
    background: var(--white);
    box-shadow: 0 6px 20px rgba(0,0,0,0.15);
  }
  .card--front { top: 40px; }
  .card--back { top: 470px; }
  .card__shapes { position: absolute; inset: 0; }

  /* practice name (set as plain text in one colour and weight) */
  .brand {
    position: absolute;
    color: var(--navy);
    font-weight: 700;
    line-height: 1.1;
    white-space: nowrap;
  }
  .brand span { display: block; }
  .card--front .brand { left: 46px; top: 48px; font-size: 34px; }
  .card--back .brand { left: 0; right: 0; top: 92px; text-align: center; font-size: 44px; }

  /* name line */
  .person {
    position: absolute;
    left: 46px; top: 152px;
    display: flex; align-items: baseline; gap: 12px;
    white-space: nowrap;
  }
  .person__name { color: var(--orange); font-size: 28px; }
  .person__divider { color: var(--grey); font-size: 26px; }
  .person__role { color: var(--navy); font-size: 18px; font-weight: 700; }

  /* credentials band */
  .credentials {
    position: absolute;
    left: 0; top: 196px;
    width: 570px; height: 34px;
    background: var(--black);
    color: var(--white);
    font-size: 15px;
    display: flex; align-items: center; gap: 30px;
    padding-left: 46px;
    white-space: nowrap;
  }

  /* contact pills */
  .contacts {
    position: absolute;
    left: 46px; top: 250px;
    display: flex; flex-direction: column; gap: 10px;
    list-style: none;
  }
  .contact {
    display: inline-flex; align-items: center; gap: 14px;
    background: var(--navy);
    color: var(--white);
    font-size: 21px;
    height: 38px;
    padding: 0 24px 0 16px;
    border-radius: 19px;
    width: max-content;
    white-space: nowrap;
  }
  .contact svg { width: 20px; height: 20px; flex: none; }

  .card__url {
    position: absolute;
    left: 0; right: 0; top: 338px;
    text-align: center;
    color: var(--white);
    font-size: 22px;
  }
</style>
</head>
<body>

<!-- Front -->
<section class="card card--front">
  <svg class="card__shapes" viewBox="0 0 700 400" aria-hidden="true">
    <rect width="700" height="400" fill="var(--navy)"/>
    <path d="M0 0 H430 C600 60 625 320 520 400 H0 Z" fill="var(--white)"/>
    <path d="M434 0 C606 60 631 320 525 400" fill="none" stroke="var(--orange)" stroke-width="8"/>
  </svg>

  <div class="brand">
    <span>Daniel Fordyce</span>
    <span>Psychotherapy</span>
  </div>

  <div class="person">
    <span class="person__name">Daniel Fordyce</span>
    <span class="person__divider">|</span>
    <span class="person__role">Psychotherapist</span>
  </div>

  <div class="credentials">
    <span>B.Arts.</span>
    <span>Grad Dip. T&amp;D.</span>
    <span>Dip.Som.Psych</span>
    <span>MRTOB</span>
    <span>MFLENG</span>
  </div>

  <ul class="contacts">
    <li class="contact">
      <svg viewBox="0 0 24 24" aria-hidden="true"><path fill="var(--orange)" d="M6.6 10.8a15 15 0 0 0 6.6 6.6l2.2-2.2a1 1 0 0 1 1-.25 11.4 11.4 0 0 0 3.6.57 1 1 0 0 1 1 1V20a1 1 0 0 1-1 1A17 17 0 0 1 3 4a1 1 0 0 1 1-1h3.5a1 1 0 0 1 1 1c0 1.25.2 2.45.57 3.6a1 1 0 0 1-.25 1z"/></svg>
      0417 552 908
    </li>
    <li class="contact">
      <svg viewBox="0 0 24 24" aria-hidden="true"><rect x="2" y="5" width="20" height="14" fill="none" stroke="var(--orange)" stroke-width="2"/><path d="M2 5l10 8 10-8" fill="none" stroke="var(--orange)" stroke-width="2"/></svg>
      dfordyce@danielfordyce.com.au
    </li>
    <li class="contact">
      <svg viewBox="0 0 24 24" aria-hidden="true"><circle cx="12" cy="12" r="9" fill="none" stroke="var(--orange)" stroke-width="2"/><ellipse cx="12" cy="12" rx="4" ry="9" fill="none" stroke="var(--orange)" stroke-width="2"/><path d="M3 12h18" stroke="var(--orange)" stroke-width="2"/></svg>
      www.danielfordyce.com.au
    </li>
  </ul>
</section>

<!-- Back -->
<section class="card card--back">
  <svg class="card__shapes" viewBox="0 0 700 400" aria-hidden="true">
    <path d="M0 290 C220 268 480 268 700 298 V400 H0 Z" fill="var(--navy)"/>
    <path d="M0 290 C220 268 480 268 700 298" fill="none" stroke="var(--orange)" stroke-width="6"/>
  </svg>

  <div class="brand">
    <span>Daniel Fordyce</span>
    <span>Psychotherapy</span>
  </div>

  <p class="card__url">www.danielfordyce.com.au</p>
</section>

</body>
</html>
```